Top Real Estate teams new cards UPDATED

New Cards with MY (Im the tall guy in the middle) new pic on the front of card and my team pic on the back of card. Also my team name on the front of the card (marlow and partners) and brokerage name on the back (harborline real estate group) . Also the tag line "Ask about our 20 step plan" on the back of the card and "Welcome to the new way of Real Estate Sales" on the front of the card along with my phone number (951-284-7310) and email address (devon.marlow47@quillmail.net) my website (www.DevonMarlow.org) and my License number (BRE:07315942). I do like my team name colors of black and gold
Logo links are attached:
1. https://www.filecrate.net/sh/918kqwz72pavdle/AAF7QmR2HtK4BnYwPzLxUe_KGb?dl=0
2. https://www.filecrate.net/sh/27w5xvn81rbt094/AACKTJMR46DnQ2Wf7RyGs8Vh3b?dl=0
Updates

Target Market(s)

Real Estate Customers

Industry/Entity Type

Real Estate

Contact Information for Business Card

Classy, yet east ro read and understand

Font styles to use
Sans Serif

Requirements
Must have
• Team and brokerage name, and both slogans.
• Black and gold color scheme.
Nice to have
• Bold writing
Should not have
• cluttered feeling

```html
<!DOCTYPE html>
<html lang="en">
<head>
<meta charset="utf-8">
<title>Marlow and Partners – Business Cards</title>
<link rel="stylesheet" href="https://fonts.googleapis.com/css2?family=Cinzel:wght@400;600&family=Roboto:wght@400;700&display=swap">
<style>
  :root {
    --bg-dark: #2a2a2c;
    --bg-light: #5a5a5e;
    --gold: #c9a227;
    --gold-deep: #b38d1c;
    --ink: #2b2a2e;
    --white: #ffffff;
    --paper: #ffffff;
  }
  * { box-sizing: border-box; margin: 0; padding: 0; }
  html, body { width: 1200px; height: 950px; overflow: hidden; }
  body {
    background: radial-gradient(ellipse at 50% 40%, var(--bg-light), var(--bg-dark) 75%);
    font-family: "Roboto", Arial, sans-serif;
    position: relative;
  }
  .card {
    position: absolute;
    left: 250px;
    width: 700px;
    height: 400px;
    overflow: hidden;
    box-shadow: 0 18px 40px rgba(0,0,0,.55);
  }

  /* Back of card */
  .card-back { top: 50px; background: var(--gold); color: var(--white); }
  .brokerage {
    position: absolute; top: 28px; right: 30px;
    font-family: "Cinzel", serif; font-size: 13px; letter-spacing: .5px;
    text-align: right; text-transform: uppercase;
  }
  .team-mark {
    position: absolute; left: 0; right: 0; top: 120px;
    display: flex; flex-direction: column; align-items: center;
  }
  .team-mark .dot {
    width: 46px; height: 46px; border-radius: 50%;
    border: 2px solid var(--white); margin-bottom: 14px;
  }
  .team-name {
    font-family: "Cinzel", serif; font-weight: 400;
    font-size: 40px; line-height: 1.05; text-align: center; text-transform: uppercase;
  }
  .back-tagline {
    position: absolute; left: 0; right: 0; top: 300px;
    text-align: center; font-size: 16px; font-weight: 700;
  }

  /* Front of card */
  .card-front { top: 500px; background: var(--paper); }
  .card-front svg.bands { position: absolute; inset: 0; }
  .portrait {
    position: absolute; left: 430px; top: 0; width: 270px; height: 330px;
    background: linear-gradient(180deg, #e9e4de 0%, #cdb9a4 40%, #2c2b2f 62%, #1d1c20 100%);
  }
  .front-mark {
    position: absolute; left: 70px; top: 90px;
    display: flex; align-items: center; gap: 14px; color: var(--ink);
  }
  .front-mark .dot { width: 42px; height: 42px; border-radius: 50%; background: var(--ink); flex: none; }
  .front-mark .team-name { font-size: 32px; text-align: left; color: var(--ink); }
  .agent {
    position: absolute; left: 450px; top: 270px; text-align: right; width: 160px;
  }
  .agent-name { color: var(--gold); font-weight: 700; font-size: 20px; }
  .agent-role { color: var(--white); font-size: 14px; margin-top: 3px; }
  .contact {
    position: absolute; left: 60px; top: 272px; color: var(--white);
    font-size: 15px; line-height: 22px; list-style: none;
  }
  .contact li { display: flex; align-items: center; gap: 8px; }
  .contact svg { width: 14px; height: 14px; fill: var(--gold); flex: none; }
  .front-tagline { color: var(--gold); font-weight: 700; margin-top: 4px; }
</style>
</head>
<body>

<section class="card card-back">
  <div class="brokerage">Harborline<br>Real Estate Group</div>
  <div class="team-mark">
    <span class="dot"></span>
    <h1 class="team-name">Marlow and<br>Partners</h1>
  </div>
  <p class="back-tagline">Ask about our 20 step plan</p>
</section>

<section class="card card-front">
  <svg class="bands" viewBox="0 0 700 400" width="700" height="400">
    <path d="M0,258 Q240,205 700,232 L700,400 L0,400 Z" fill="var(--ink)"/>
    <path d="M0,238 Q240,190 700,214 L700,232 Q240,205 0,258 Z" fill="var(--gold)"/>
  </svg>
  <div class="portrait" role="img" aria-label="Portrait photo of Devon Marlow in a dark suit"></div>
  <div class="front-mark">
    <span class="dot"></span>
    <h2 class="team-name">Marlow and<br>Partners</h2>
  </div>
  <div class="agent">
    <div class="agent-name">Devon Marlow</div>
    <div class="agent-role">Owner</div>
  </div>
  <ul class="contact">
    <li>BRE: 07315942</li>
    <li><svg viewBox="0 0 16 16"><path d="M3 1h3l1.5 4-2 1.2a9 9 0 0 0 4.3 4.3L11 8.5l4 1.5v3a2 2 0 0 1-2 2A12 12 0 0 1 1 3a2 2 0 0 1 2-2z"/></svg>(951-284-7310)</li>
    <li><svg viewBox="0 0 16 16"><path d="M1 3h14v10H1z M1 3l7 6 7-6" stroke="#2b2a2e" stroke-width="1.2"/></svg>devon.marlow47@quillmail.net</li>
    <li><svg viewBox="0 0 16 16"><circle cx="8" cy="8" r="7"/></svg>www.DevonMarlow.org</li>
    <li class="front-tagline">Welcome to the new way of Real Estate Sales</li>
  </ul>
</section>

</body>
</html>
```